Flyer für eine Imkerei
Wunderbare unkomplizierte Zusammenarbeit mit einem tollen Designer. Extrem gutes Verständnis der Grundidee, super flexibles einarbeiten eigener Verbesserungsvorschläge - einfach sehr kompetent! Danke dafür.
Zielgruppe
Ich bin Hobbyimker mit einer sehr kleinen Imkerei im Dorf. Ich biete lokalen Honig an. Der Flyer soll ein Infoflyer für Kunden und evt. Neukunden sein.
Aufgabenstellung
Bitte im Wickelfalz hochkant A4, (gefaltet also 99x210). Textbausteine sind als Datei angehängt. Bitte nur den Text nutzen, nicht Schriftgröße, Schritart etc. Ebenso ist eigenes Bildmaterial vorhanden. Ich würde mich über ein edles aber schlicht modernes Design freuen. Das Design darf gern Honigwaben (Hexagon) als Grundidee beinhalten. Bevorzugte Farbtöne sind schwarz, gold, gelb, orange (honigfarben) bis Weinrot (siehe Honigetikett auf dem Foto).

```html
<!DOCTYPE html>
<html lang="de">
<head>
<meta charset="utf-8">
<title>Flyer Imkerei Saaletal</title>
<link rel="stylesheet" href="https://fonts.googleapis.com/css2?family=Roboto:wght@400;500;700;900&display=swap">
<style>
:root{
  --bg:#a8a8a8;
  --black:#0c0c0c;
  --white:#ffffff;
  --paper:#f4f4f4;
  --orange:#f39200;
  --gold:#f5aa1c;
  --yellow:#f7d44c;
  --rust:#c0501c;
  --text:#222222;
}
*{box-sizing:border-box;margin:0;padding:0}
html,body{width:1200px;height:2317px;overflow:hidden}
body{background:var(--bg);font-family:"Roboto",Arial,sans-serif;position:relative}
.sheet{position:absolute;left:30px;width:1140px;height:805px;display:flex;box-shadow:0 6px 18px rgba(0,0,0,.35);overflow:hidden;background:var(--black)}
.sheet--outside{top:250px}
.sheet--inside{top:1260px}
.panel{position:relative;width:380px;height:100%}
.abs{position:absolute}
.center{text-align:center;left:0;right:0}
.orange{color:var(--orange)}

/* outside */
.about{background:var(--white);height:250px}
.about__title{top:44px;font-size:19px;font-weight:500}
.about__lead{top:76px;font-size:11.5px;font-weight:700;line-height:1.45}
.about__body{top:122px;left:18px;right:18px;font-size:10.6px;font-weight:700;line-height:1.55;color:var(--text)}
.photo{display:block}
.photo--bottles{top:238px;left:0;width:380px;height:350px;background:linear-gradient(180deg,#f0a51a 0%,#c7650c 45%,#6b2a06 75%,var(--black) 100%)}
.gentle__title{top:574px;font-size:18px;font-weight:500}
.gentle__body{top:610px;left:30px;right:30px;font-size:11.3px;font-weight:700;line-height:1.62;color:var(--white)}
.photo--cover{top:0;left:380px;width:760px;height:640px;background:linear-gradient(180deg,#3d4a25 0%,#6a4a6a 25%,#c27b1c 55%,#7a3a0a 80%,var(--black) 100%);position:absolute}
.taste{top:456px;left:28px;width:326px;height:142px;background:var(--orange);border-radius:8px;color:var(--black);padding:16px 14px 0;text-align:center}
.taste h3{font-size:22px;font-weight:700;margin-bottom:6px}
.taste p{font-size:11.6px;line-height:1.55}
.contact__addr{top:632px;font-size:11px;color:var(--white)}
.contact__order{top:658px;font-size:14.5px;font-weight:700;line-height:1.3}
.contact__phone{top:704px;font-size:29px;font-weight:900;letter-spacing:1.5px}
.contact__note{top:755px;font-size:11px;color:var(--white)}
.cover__title{top:628px;font-size:25px;font-weight:700;line-height:1.2;text-transform:uppercase}
.cover__sub{top:694px;font-size:15px;color:var(--white);letter-spacing:.3px}
.cover__sender{top:733px;font-size:11px;color:var(--white);line-height:1.55}

/* inside */
.panel--light{background:var(--paper)}
.photo--top{top:0;left:0;width:380px;height:222px}
.photo--basil{background:linear-gradient(160deg,#2f3d1c,#6f5a6c 50%,#3a4a22)}
.photo--hive{background:linear-gradient(160deg,#cfc4a6,#4a3620 45%,#a8946a)}
.photo--flower{background:linear-gradient(160deg,#3c5a1c,#f0d21c 45%,#5a7020)}
.tab{top:208px;left:60px;width:250px;height:32px;border-radius:16px;background:var(--orange);color:var(--white);font-size:15px;font-weight:700;text-align:center;line-height:32px}
.honey__lead{top:262px;left:43px;width:300px;font-size:11.4px;font-weight:700;line-height:1.5}
.variety{left:46px;width:283px;height:28px;border:2px solid var(--orange);border-radius:14px;font-size:11.5px;font-weight:700;text-align:center;line-height:24px;color:var(--text);background:var(--white)}
.variety--spring{top:323px}
.variety--summer{top:460px}
.variety__text{left:43px;width:300px;font-size:10.8px;line-height:1.6;color:var(--text)}
.variety__text--spring{top:364px}
.variety__text--summer{top:501px}
.tip{top:592px;left:43px;width:300px;height:114px;background:linear-gradient(180deg,var(--gold),var(--orange));border-radius:6px;font-size:10.8px;line-height:1.5;color:var(--black);text-align:center;padding:12px 14px}
.heading{top:280px;font-size:18.5px;font-weight:700}
.list{list-style:none}
.list li{position:absolute;padding-left:30px}
.list svg{position:absolute;left:0;top:2px;width:14px;height:14px}
.list b{display:block;font-size:11px;color:var(--orange);font-weight:700;margin-bottom:3px;line-height:1.35}
.list span{font-size:10.8px;line-height:1.6;display:block}
.list--regional li{left:33px;width:320px;color:var(--text)}
.list--regional li+li{border-top:1px solid #bbb}
.list--facts li{left:60px;width:275px;color:var(--white)}
.combs{left:0;bottom:0;width:1140px;height:52px;background:linear-gradient(180deg,var(--yellow) 0%,var(--gold) 40%,var(--orange) 70%,var(--rust) 100%);position:absolute}
</style>
</head>
<body>

<section class="sheet sheet--outside">
  <div class="panel">
    <div class="abs about" style="left:0;top:0;width:380px"></div>
    <h2 class="abs center about__title orange">Über uns</h2>
    <p class="abs center about__lead orange">Herzlich willkommen in unserer kleinen<br>Hobbyimkerei im schönen Saaletal!</p>
    <p class="abs center about__body">Bei uns erhalten Sie alles aus einer Hand.<br>Von der sorgsamen Pflege der sensiblen Bienenvölker über die Honigernte bis hin zum fertig etikettierten Glas wird jeder Arbeitsschritt persönlich vor Ort mit größter Sorgfalt ausgeführt, um ein reines und unverfälschtes Naturprodukt zu garantieren</p>
    <div class="abs photo photo--bottles" role="img" aria-label="Foto: Honig in Glasflaschen vor Wabenmuster"></div>
    <h3 class="abs center gentle__title orange">Natürlich und schonend</h3>
    <p class="abs center gentle__body">Wir betreiben eine sanfte und wesensgemäße Bienenhaltung. Die Bienenstöcke haben einen festen Standort auf einer sonnigen Waldlichtung. Sie werden im Saisonverlauf nicht transportiert, sondern sammeln den Nektar der Pflanzen, die hier im Saaletal ganz natürlich saisonal blühen. Das garantiert einen authentischen Honig aus unserer Heimat.</p>
  </div>
  <div class="photo--cover" role="img" aria-label="Foto: Biene auf Blüte über gestapelten Gläsern Blütenhonig"></div>
  <div class="panel">
    <div class="abs taste">
      <h3>Probieren Sie selbst!</h3>
      <p><b>Wurde Ihre Neugier geweckt?</b> Dann freuen wir uns, wenn Sie den reinen Geschmack unseres lokalen Produktes probieren möchten.<br>Unser Honig ist vor Ort erhältlich.</p>
    </div>
    <p class="abs center contact__addr">Familie XYZ Straße 100000 Stadt</p>
    <p class="abs center contact__order orange">Für Bestellungen und Abholungen<br>erreichen Sie uns unter:</p>
    <p class="abs center contact__phone orange">X-XXX-XXXXXXX</p>
    <p class="abs center contact__note">Schauen Sie gern vorbei. Wir freuen uns auf Sie!</p>
  </div>
  <div class="panel">
    <h1 class="abs center cover__title orange">Feinster Honig aus<br>dem Saaletal</h1>
    <p class="abs center cover__sub">NATÜRLICH, REGIONAL &amp; DIREKT</p>
    <p class="abs center cover__sender">Family XYZ<br>Stadt XYZ</p>
  </div>
</section>

<section class="sheet sheet--inside">
  <div class="panel panel--light">
    <div class="abs photo photo--top photo--basil" role="img" aria-label="Foto: Biene an lila Blüten"></div>
    <div class="abs tab">UNSER HONIG</div>
    <p class="abs honey__lead orange">Durch den festen Standort können mit zwei Honigernten im Jahr folgende Sorten angeboten werden, die den Geschmack der Saison einfangen:</p>
    <div class="abs variety variety--spring">Frühtracht – cremig</div>
    <p class="abs variety__text variety__text--spring">Gesammelt von den ersten Blüten des Jahres - vorwiegend Obstblüte und Raps. Für eine streichzarte Konsistenz wird dieser milde, blumige Honig vor dem Abfüllen fein-cremig gerührt.</p>
    <div class="abs variety variety--summer">Sommerblüte – flüssig &amp; cremig</div>
    <p class="abs variety__text variety__text--summer">Ein etwas kräftigerer und aromatischer Honig aus den Blüten des Hochsommers – vorwiegend Linde. Diesen Honig gibt es je nach Verfügbarkeit als flüssige Variante oder ebenfalls fein-cremig gerührt.</p>
    <div class="abs tip"><b>Gut zu wissen:</b> Echter Honig kann kristallisieren. Das ist ein natürlicher Prozess und ein Zeichen für hohe Qualität.<br>Im Wasserbad bei maximal 40°C wird er schonend wieder flüssig. Honig bitte kühl, trocken und dunkel lagern.</div>
  </div>
  <div class="panel panel--light">
    <div class="abs photo photo--top photo--hive" role="img" aria-label="Foto: Bienen am Flugloch des Bienenstocks"></div>
    <div class="abs tab" style="left:65px">WARUM REGIONAL?</div>
    <h2 class="abs heading orange" style="left:33px">Gutes für Sie und unsere Heimat</h2>
    <ul class="list list--regional">
      <li style="top:330px"><svg viewBox="0 0 14 14"><circle cx="7" cy="7" r="7" fill="#f39200"/><path d="M4 7.2l2 2 4-4.4" stroke="#fff" stroke-width="1.8" fill="none"/></svg><b>Für die Natur vor unserer Haustür</b><span>Unsere Bienen bestäuben unzählige Pflanzen im Saaletal und sorgen so für den Erhalt der Artenvielfalt.</span></li>
      <li style="top:406px;padding-top:12px"><svg viewBox="0 0 14 14" style="top:14px"><circle cx="7" cy="7" r="7" fill="#f39200"/><path d="M4 7.2l2 2 4-4.4" stroke="#fff" stroke-width="1.8" fill="none"/></svg><b>Absolute Transparenz</b><span>Keine langen Transportwege, keine undurchsichtigen Lieferketten. Der Honig kommt direkt vom Bienenstock im Wald in Ihr Glas. Der Erlös kommt zu 100% unserer Imkerei zugute.</span></li>
      <li style="top:522px;padding-top:12px"><svg viewBox="0 0 14 14" style="top:14px"><circle cx="7" cy="7" r="7" fill="#f39200"/><path d="M4 7.2l2 2 4-4.4" stroke="#fff" stroke-width="1.8" fill="none"/></svg><b>Der Geschmack der Heimat</b><span>Jeder Löffel fängt den einzigartigen Geschmack der vielfältigen lokalen Pflanzenwelt des Saaletals ein.</span></li>
      <li style="top:604px;padding-top:12px"><svg viewBox="0 0 14 14" style="top:14px"><circle cx="7" cy="7" r="7" fill="#f39200"/><path d="M4 7.2l2 2 4-4.4" stroke="#fff" stroke-width="1.8" fill="none"/></svg><b>Geprüfte Qualität</b><span>Unser Honig wird regelmäßig in einem Fachlabor auf Qualität und Zusammensetzung untersucht. Die Analyse der Pollen bestätigt dabei die botanische und geografische Herkunft – eine Garantie für echten Honig aus der Region.</span></li>
    </ul>
  </div>
  <div class="panel">
    <div class="abs photo photo--top photo--flower" role="img" aria-label="Foto: Biene auf gelber Blüte"></div>
    <div class="abs tab" style="left:40px;width:290px">FASZINIERENDE BIENENWELT</div>
    <h2 class="abs heading orange" style="left:64px">Wussten Sie schon?</h2>
    <ul class="list list--facts">
      <li style="top:330px"><svg viewBox="0 0 14 14"><circle cx="7" cy="7" r="7" fill="#f39200"/><path d="M4 7.2l2 2 4-4.4" stroke="#0c0c0c" stroke-width="1.8" fill="none"/></svg><b>Bienen sind echte Vielflieger!</b><span>Für Ihr 500g-Glas Honig legen sie eine Flugstrecke hin, die dreimal um die Erde reicht.</span></li>
      <li style="top:432px"><svg viewBox="0 0 14 14"><circle cx="7" cy="7" r="7" fill="#f39200"/><path d="M4 7.2l2 2 4-4.4" stroke="#0c0c0c" stroke-width="1.8" fill="none"/></svg><b>Sie verschenken ihr Lebenswerk!</b><span>Eine Biene produziert in ihrem ganzen Leben nur etwa einen halben Teelöffel Honig. Genießen Sie den Honig bewusst – es steckt viel Arbeit drin!</span></li>
      <li style="top:552px"><svg viewBox="0 0 14 14"><circle cx="7" cy="7" r="7" fill="#f39200"/><path d="M4 7.2l2 2 4-4.4" stroke="#0c0c0c" stroke-width="1.8" fill="none"/></svg><b>Im Bienenstock regiert eine knallharte Chefin!</b><span>Im Sommer legt die Königin bis zu 2.000 Eier pro Tag. Das ist mehr als ihr eigenes Körpergewicht. Ein wahrhaft produktives Management.</span></li>
    </ul>
  </div>
  <div class="combs" role="img" aria-label="Wabenband in Gelb, Orange und Rostrot"></div>
</section>

</body>
</html>
```